Creative & Professional Business Card for hair salon

We are looking to update our business cards. Our salon is creative, modern, progressive and professional and looking for a design that will reflect this.

```html
<!DOCTYPE html>
<html lang="en">
<head>
<meta charset="utf-8">
<title>Silver Comb Studio – Appointment Card</title>
<link rel="stylesheet" href="https://fonts.googleapis.com/css2?family=Abel&display=swap">
<style>
  :root {
    --page: #ffffff;
    --card: #e8e8ea;
    --ink: #1d3f73;
    --rule: #5e9cc2;
  }
  html, body {
    margin: 0;
    padding: 0;
    width: 1200px;
    height: 804px;
    overflow: hidden;
    background: var(--page);
  }
  .canvas {
    position: relative;
    width: 1200px;
    height: 804px;
    font-family: "Abel", "Arial Narrow", sans-serif;
    color: var(--ink);
  }
  .card {
    position: absolute;
    left: 40px;
    top: 40px;
    width: 1120px;
    height: 725px;
    background: var(--card);
  }
  .card-lines {
    position: absolute;
    left: 0;
    top: 0;
    width: 1200px;
    height: 804px;
  }
  .card-lines line {
    stroke: var(--rule);
    stroke-width: 1.3;
  }
  .appointment-heading {
    position: absolute;
    left: 0;
    width: 1200px;
    top: 160px;
    margin: 0;
    text-align: center;
    font-weight: 400;
    font-size: 50px;
    letter-spacing: 3px;
    line-height: 60px;
  }
  .contact-list {
    position: absolute;
    left: 0;
    width: 1200px;
    top: 478px;
    margin: 0;
    padding: 0;
    list-style: none;
    text-align: center;
    font-size: 37px;
    letter-spacing: 2.4px;
    line-height: 60px;
  }
</style>
</head>
<body>
<div class="canvas">
  <div class="card"></div>

  <svg class="card-lines" viewBox="0 0 1200 804" aria-hidden="true">
    <!-- top frame -->
    <line x1="70" y1="67" x2="1131" y2="67"/>
    <line x1="70" y1="67" x2="70" y2="130"/>
    <line x1="1131" y1="67" x2="1131" y2="130"/>
    <!-- bottom corners -->
    <line x1="66" y1="676" x2="66" y2="739"/>
    <line x1="66" y1="739" x2="130" y2="739"/>
    <line x1="1135" y1="676" x2="1135" y2="739"/>
    <line x1="1071" y1="739" x2="1135" y2="739"/>
    <!-- appointment write-in rule -->
    <line x1="251" y1="399" x2="949" y2="399"/>
    <line x1="251" y1="407" x2="949" y2="407"/>
  </svg>

  <h1 class="appointment-heading">Your next appointment is</h1>

  <ul class="contact-list">
    <li class="contact-phone">07 5550 1234</li>
    <li class="contact-email">hello@silvercombstudio.com.au</li>
    <li class="contact-social">www.socialpage.com/SilverCombStudioByAlexMore</li>
  </ul>
</div>
</body>
</html>
```